Wochen Speiseplan
Zielgruppe
Hospiz
Aufgabenstellung
Wir brauchen für unser Hospiz einen Wochenspeiseplan. Es soll eine Powerpointseite im A4 Format erstellt werden. Wir brauchen 4 unterschiedliche Seiten - für jede Jahreszeit einen Entwurf. Der Speiseplan soll von uns selbst ausgefüllt werden können.
Inhalte: Montag - Sonntag jeweils Mittag- und Abendessen. (Aufgebaut wie ein Stundenplan.). Möglichst große Schriftgröße. In der Fußnote bitte: "Änderungen vorbehalten schreiben". Das ganze soll professionell, aber dennoch liebevoll gestaltet sein. Es soll unseren Bewohnern "Liust machen" draufzuschauen. Der Plan wird jede Woche neu ausgefüllt, ausgedruckt und laminiert. Sollte also einfach zu handhaben sein.
Das Hospiz lebt von Spenden, daher bitte nicht zu aufwendig, dafür aber bezahlbar machen.

```html
<!DOCTYPE html>
<html lang="de">
<head>
<meta charset="utf-8">
<title>Wochenspeiseplan</title>
<link rel="stylesheet" href="https://fonts.googleapis.com/css2?family=Sniglet&family=Crimson+Text:wght@400&family=Noto+Sans:ital,wght@0,400;1,700&display=swap">
<style>
  :root {
    --leaf: #7ab800;
    --leaf-dark: #5e9000;
    --meadow: #b9d46c;
    --meadow-light: #cfe29a;
    --ring-tint: #e4efc6;
    --olive: #4f5f2a;
    --row-lunch: #c6d89c;
    --row-dinner: #d8e5b6;
    --ink: #2b2b22;
    --paper: #ffffff;
  }
  * { margin: 0; padding: 0; box-sizing: border-box; }
  html, body { width: 1200px; height: 900px; overflow: hidden; background: var(--paper); }
  .menu-board {
    position: relative;
    width: 1200px;
    height: 900px;
    overflow: hidden;
    font-family: "Noto Sans", Verdana, sans-serif;
    color: var(--ink);
    background: var(--paper);
  }
  .ring-pattern {
    position: absolute;
    left: 0; top: 0;
    width: 1200px; height: 330px;
    background: linear-gradient(180deg, var(--ring-tint) 0%, #f1f7e0 70%, var(--meadow-light) 100%);
  }
  .meadow {
    position: absolute;
    left: 0; top: 300px;
    width: 1200px; height: 600px;
    background: linear-gradient(180deg, var(--meadow-light) 0%, var(--meadow) 25%, var(--meadow) 100%);
  }
  .title-banner {
    position: absolute;
    left: 0; top: 0;
    width: 1200px; height: 300px;
  }
  .title {
    position: absolute;
    left: 285px; top: 42px;
    font-family: "Sniglet", "Comic Sans MS", cursive;
    font-size: 92px;
    font-weight: 400;
    color: var(--paper);
    letter-spacing: -1px;
    transform: rotate(-1deg);
  }
  .greeting {
    position: absolute;
    left: 445px; top: 176px;
    font-family: "Crimson Text", Georgia, serif;
    font-size: 31px;
    color: var(--paper);
    transform: rotate(-5deg);
    transform-origin: left center;
  }
  .meal-table {
    position: absolute;
    left: 42px; top: 332px;
    width: 1121px;
    border-collapse: collapse;
    table-layout: fixed;
  }
  .meal-table th, .meal-table td {
    border: 2px solid var(--paper);
    text-align: left;
    vertical-align: top;
  }
  .meal-table th {
    background: var(--olive);
    color: var(--paper);
    font-style: italic;
    font-weight: 700;
    font-size: 25px;
    height: 46px;
    padding: 4px 10px;
  }
  .meal-table td {
    font-size: 21px;
    line-height: 28px;
    padding: 8px 10px;
  }
  .lunch td { background: var(--row-lunch); height: 209px; }
  .dinner td { background: var(--row-dinner); height: 206px; }
  .footnote {
    position: absolute;
    right: 42px; top: 810px;
    font-style: italic;
    font-weight: 700;
    font-size: 20px;
    color: var(--ink);
  }
</style>
</head>
<body>
<main class="menu-board">
  <div class="ring-pattern" role="img" aria-label="Dekoratives Muster aus hellgrünen Ringen"></div>
  <div class="meadow" role="img" aria-label="Hellgrüner Hintergrund mit stilisierten Blumenornamenten"></div>

  <svg class="title-banner" viewBox="0 0 1200 300" aria-hidden="true">
    <polygon points="250,0 1200,0 1200,210 282,285" fill="var(--leaf-dark)" opacity="0.35" transform="translate(6,6)"/>
    <polygon points="242,0 1200,0 1200,205 275,280" fill="var(--leaf)"/>
  </svg>
  <h1 class="title">Wochenspeiseplan</h1>
  <p class="greeting">Wir wünschen einen guten Appetit!</p>

  <table class="meal-table">
    <colgroup>
      <col style="width:170px"><col style="width:178px"><col style="width:155px"><col style="width:155px"><col style="width:155px"><col style="width:153px"><col style="width:155px">
    </colgroup>
    <thead>
      <tr><th>Mo</th><th>Di</th><th>Mi</th><th>Do</th><th>Fr</th><th>Sa</th><th>So</th></tr>
    </thead>
    <tbody>
      <tr class="lunch">
        <td>Spaghetti Bolognese</td>
        <td>Gemüse-<br>pfanne mit Hähnchen-<br>brust</td>
        <td>Milchreis mit Zucker/<br>Zimt<br>und Kirsch-<br>kompott</td>
        <td>Nudelein-<br>topf mit Geflügel-<br>fleisch</td>
        <td>Germ-<br>knödel mit Pflaume-<br>mus-<br>füllung</td>
        <td>3 gekochte Eier mit Senfsoße und Kartoffeln</td>
        <td>Linsenein-<br>topf mit Bockwurst, Fladenbrot</td>
      </tr>
      <tr class="dinner">
        <td>Chicken Wrap mit buntem Salat und Guacamole</td>
        <td>Gebratener Seehecht in Ei-Hülle dazu Kartoffel-<br>püree</td>
        <td>Frikadelle schwä-<br>bische Art auf Kräuter-<br>spätzle</td>
        <td>Gegrillte Schweins-<br>haxe</td>
        <td>Nudel-<br>Schinken-<br>Gratin dazu gemischter Salat</td>
        <td>Kartoffel-<br>rösti mit Tomaten-<br>Schnitt-<br>lauch-<br>Quark</td>
        <td>Kochklopse Königs-<br>berger Art mit Kartoffeln/<br>Reis</td>
      </tr>
    </tbody>
  </table>

  <p class="footnote">Änderungen vorbehalten</p>
</main>
</body>
</html>
```